KV Holding ltd*

I need a full website designed for for a 10,000m2 strorage facity which specialize in heavy commercial storage

it needs to be in english please

Target Market(s)

Comercial sector

Industry/Entity Type

Construction Company

Logo Text

KV

Coding

Coded - Design and coding required

Number of Pages Required

1 page

Font styles to use
Sans Serif

Colors
ec1f27
ffffff

Requirements
Must have
• Tel 0064 218846097
• email- lewis@kvholding.co.nz
Nice to have
• We specilize in large items with the facilty have 3 15tonne Gantry cranes and heavy mobile lifting equipment we can store items up to 20 tonne and we are fully covered and secure.
• square meter rates from 20m2 to 10,000 m2

```html
<!DOCTYPE html>
<html lang="en">
<head>
<meta charset="utf-8">
<title>KV Holding – Heavy Commercial Storage</title>
<link rel="stylesheet" href="https://fonts.googleapis.com/css2?family=Rajdhani:wght@400;500;600&family=Montserrat:wght@400;500;600&display=swap">
<style>
:root{
  --red:#ec1f27;
  --white:#ffffff;
  --black:#000000;
  --ink:#222222;
  --muted:#555555;
  --grey:#6d6d6f;
  --grey-dark:#5b5b5d;
  --line:#e6e6e6;
}
*{box-sizing:border-box;margin:0;padding:0}
html,body{width:1200px;height:3750px;overflow:hidden}
body{position:relative;font-family:'Montserrat',sans-serif;color:var(--ink);background:var(--white)}
.abs{position:absolute}
h1,h2,h3{font-family:'Rajdhani',sans-serif;font-weight:500}
.btn{position:absolute;display:flex;align-items:center;justify-content:center;background:var(--red);color:var(--white);border-radius:20px;font-size:14px;font-family:'Montserrat',sans-serif}
.photo{position:absolute}

/* header */
.site-header{position:absolute;left:0;top:0;width:1200px;height:145px;background:var(--black)}
.brand{position:absolute;left:76px;top:56px;display:flex;align-items:center;gap:10px;color:var(--red);font-family:'Rajdhani',sans-serif;font-weight:600;font-size:26px;letter-spacing:2px}
.brand .dot{width:14px;height:14px;background:var(--red);border-radius:50%}
.contact-bar{position:absolute;top:37px;right:74px;display:flex;gap:24px;color:var(--white);font-size:13px}
.contact-bar span{display:flex;align-items:center;gap:10px}
.icon-badge{width:30px;height:30px;border-radius:50%;background:var(--red);display:flex;align-items:center;justify-content:center}
.main-nav{position:absolute;top:89px;right:72px;display:flex;gap:48px;font-size:13px;color:var(--white)}
.main-nav .active{color:var(--red)}

/* hero */
.hero{position:absolute;left:0;top:145px;width:1200px;height:588px;background:linear-gradient(180deg,#5a5e63 0%,#7b7466 35%,#4d4a44 70%,#2f2b27 100%)}
.hero-title{position:absolute;left:0;width:1200px;top:240px;text-align:center;color:var(--white);font-size:38px;font-family:'Rajdhani',sans-serif;font-weight:500}
.hero-text{position:absolute;left:405px;width:420px;top:290px;text-align:center;color:var(--white);font-size:13px;line-height:19px}
.hero-arrow{position:absolute;top:265px;width:38px;height:38px;border:1px solid rgba(255,255,255,.6);border-radius:50%}
.hero-tabs span{position:absolute;top:575px;width:44px;height:13px;background:var(--white)}

/* sections */
.section-title{position:absolute;font-size:36px;color:var(--ink)}
.section-title::after{content:"";position:absolute;left:0;bottom:-14px;width:90px;height:3px;background:var(--red)}
.on-grey{color:var(--white)}
.on-grey::after{background:var(--white)}
.body-text{position:absolute;font-size:12px;line-height:19.5px;color:var(--ink)}
.grey-band{position:absolute;left:0;width:1200px;background:linear-gradient(135deg,#7a7a7c,var(--grey) 50%,var(--grey-dark))}
.checklist{position:absolute;display:grid;grid-template-columns:repeat(2,auto);column-gap:28px;row-gap:19px;font-size:14px;list-style:none}
.checklist li{display:flex;gap:12px;align-items:flex-start;line-height:19px}
.checklist svg{flex:none}

/* contact */
.field{position:absolute;border:1px solid var(--line);font-size:13px;color:var(--muted);padding:12px 9px}

/* footer */
.site-footer{position:absolute;left:0;top:3370px;width:1200px;height:322px;background:var(--black);color:var(--white)}
.footer-notch span{position:absolute;top:3355px;width:44px;height:15px;background:var(--black)}
.footer-col h3{position:absolute;top:77px;font-size:19px;font-family:'Rajdhani',sans-serif;font-weight:500;color:var(--white)}
.footer-col h3::after{content:"";position:absolute;left:0;bottom:-8px;width:34px;height:2px;background:var(--white)}
.footer-links{position:absolute;left:352px;top:115px;list-style:none;font-size:13px;line-height:22.5px}
.footer-links li::before{content:">";margin-right:16px}
.footer-links .active{color:var(--red)}
.footer-info{position:absolute;left:597px;top:115px;font-size:13px;line-height:22px}
.info-row{display:flex;gap:19px;align-items:flex-start}
.info-row svg{flex:none;margin-top:4px}
.copyright{position:absolute;left:0;top:3692px;width:1200px;height:58px;background:var(--white)}
.copyright p{position:absolute;left:77px;top:22px;font-size:12px;color:var(--ink)}
.social{position:absolute;right:72px;top:16px;display:flex;gap:10px}
.social span{width:29px;height:29px;border-radius:50%;background:var(--black)}
.social span:first-child{background:var(--red)}
</style>
</head>
<body>
<svg width="0" height="0" class="abs">
  <defs>
    <symbol id="tick" viewBox="0 0 20 20"><circle cx="10" cy="10" r="8.5" fill="none" stroke="currentColor" stroke-width="1.6"/><path d="M5.5 10.2l3 3L15 6" fill="none" stroke="currentColor" stroke-width="1.8" stroke-linecap="round"/></symbol>
  </defs>
</svg>

<header class="site-header">
  <div class="brand"><i class="dot"></i>KV Holding</div>
  <div class="contact-bar">
    <span><i class="icon-badge"><svg width="14" height="10" viewBox="0 0 14 10"><rect x=".5" y=".5" width="13" height="9" fill="none" stroke="#fff"/><path d="M.5 .5l6.5 5 6.5-5" fill="none" stroke="#fff"/></svg></i>lewis@kvholding.co.nz</span>
    <span><i class="icon-badge"><svg width="14" height="14" viewBox="0 0 24 24"><path fill="#fff" d="M6.6 10.8a15 15 0 006.6 6.6l2.2-2.2c.3-.3.7-.4 1-.2 1.1.4 2.3.6 3.6.6.6 0 1 .4 1 1V20c0 .6-.4 1-1 1A17 17 0 013 4c0-.6.4-1 1-1h3.5c.6 0 1 .4 1 1 0 1.3.2 2.5.6 3.6.1.3 0 .7-.2 1z"/></svg></i>0064 218846097</span>
  </div>
  <nav class="main-nav"><span class="active">Home</span><span>About us</span><span>Storage</span><span>Workshops</span><span>Contact us</span></nav>
</header>

<section class="hero" role="img" aria-label="Warehouse interior with yellow gantry crane and mobile lifting equipment">
  <h1 class="hero-title">Welcome to KV Holding</h1>
  <p class="hero-text">10,000m2 of covered, secure heavy commercial storage with 15 tonne gantry cranes on site</p>
  <div class="btn" style="left:519px;top:340px;width:176px;height:37px">Read More</div>
  <span class="hero-arrow" style="left:25px"></span>
  <span class="hero-arrow" style="left:1133px"></span>
  <div class="hero-tabs"><span style="left:40px"></span><span style="left:128px"></span><span style="left:217px"></span><span style="left:262px"></span></div>
</section>

<section>
  <h2 class="section-title" style="left:77px;top:830px">About us</h2>
  <p class="body-text" style="left:77px;top:902px;width:510px">KV Holding is a 10,000m2 storage facility that specialises in heavy commercial storage for the construction and commercial sectors. We focus on large items: the facility has three 15 tonne gantry cranes and heavy mobile lifting equipment, so we can store items of up to 20 tonne.<br><br>Every unit is fully covered and secure, and space is charged at square metre rates from 20m2 up to 10,000m2, so you only pay for what you need.</p>
  <div class="btn" style="left:74px;top:1115px;width:176px;height:38px">Read More</div>
  <div class="abs" style="left:950px;top:1015px;width:194px;height:197px;border-right:10px solid var(--grey);border-bottom:10px solid var(--grey)"></div>
  <div class="photo" style="left:645px;top:865px;width:482px;height:332px;background:linear-gradient(135deg,#8d8f91,#54585c 60%,#3b3f43)" role="img" aria-label="Warehouse aisle with high racking and stacked pallets"></div>
</section>

<section class="grey-band" style="top:1267px;height:530px">
  <div class="photo" style="left:76px;top:84px;width:482px;height:356px;background:linear-gradient(180deg,#9ea3a6,#6c6a63 55%,#4e3a34)" role="img" aria-label="Storage hall with overhead cranes and red farm machinery"></div>
  <h2 class="section-title on-grey" style="left:628px;top:82px">STORAGE</h2>
  <p class="body-text" style="left:628px;top:155px;width:505px;color:var(--white)">Our covered halls are built for heavy plant, machinery, steel and project materials. Three 15 tonne gantry cranes and heavy mobile lifting equipment move your items in and out safely, and we can store single items of up to 20 tonne. Rent by the square metre, from 20m2 for a single machine to the full 10,000m2 for a major project.</p>
  <ul class="checklist" style="left:628px;top:284px;color:var(--white);grid-template-columns:256px 240px">
    <li><svg width="20" height="20"><use href="#tick"/></svg>Secure site at central location</li>
    <li><svg width="20" height="20"><use href="#tick"/></svg>Easy access</li>
    <li><svg width="20" height="20"><use href="#tick"/></svg>Good value rentals</li>
    <li><svg width="20" height="20"><use href="#tick"/></svg>24/7 tenants access</li>
    <li><svg width="20" height="20"><use href="#tick"/></svg>On-site manager</li>
    <li><svg width="20" height="20"><use href="#tick"/></svg>Clean, dry units</li>
    <li><svg width="20" height="20"><use href="#tick"/></svg>21 different sizes available</li>
    <li><svg width="20" height="20"><use href="#tick"/></svg>24HR alarmed &amp; monitored units available</li>
  </ul>
</section>

<section>
  <h2 class="section-title" style="left:77px;top:1910px">WORKSHOPS</h2>
  <p class="body-text" style="left:77px;top:1990px;width:510px">Workshop units for trade and construction businesses, with crane support and heavy lifting equipment available on site.</p>
  <ul class="checklist" style="left:74px;top:2047px;color:var(--ink);grid-template-columns:225px 240px">
    <li><svg width="20" height="20"><use href="#tick"/></svg>50m2 38m2 workshops</li>
    <li><svg width="20" height="20"><use href="#tick"/></svg>Smaller units available</li>
    <li><svg width="20" height="20"><use href="#tick"/></svg>Monthly rentals</li>
    <li><svg width="20" height="20"><use href="#tick"/></svg>24/7 tenants access</li>
    <li><svg width="20" height="20"><use href="#tick"/></svg>Alarmed &amp; monitored</li>
    <li><svg width="20" height="20"><use href="#tick"/></svg>Vehicle access to all units</li>
    <li><svg width="20" height="20"><use href="#tick"/></svg>Ample truck access</li>
    <li><svg width="20" height="20"><use href="#tick"/></svg>Competitive rental rates</li>
    <li><svg width="20" height="20"><use href="#tick"/></svg>Showers &amp; toilets on site</li>
  </ul>
  <div class="photo" style="left:644px;top:1872px;width:482px;height:357px;background:linear-gradient(180deg,#3c4752,#7b6a2e 40%,#8c8e91 75%,#4a4d52)" role="img" aria-label="Crane lifting steel coils inside a workshop"></div>
</section>

<section class="grey-band" style="top:2308px;height:530px">
  <div class="abs" style="left:70px;top:100px;width:490px;height:340px;background:linear-gradient(135deg,rgba(255,255,255,.16),rgba(255,255,255,.06))" role="img" aria-label="Line drawing of a storage container with dimensions 10.5 by 4.5 by 3.9"></div>
  <h2 class="abs" style="left:642px;top:127px;width:520px;font-size:37px;line-height:41px;color:var(--white)">SUITABLE FOR HOUSEHOLD, COMMERCIAL AND BUSINESSES USAGE.</h2>
  <p class="body-text" style="left:642px;top:272px;width:490px;color:var(--white)">Square metre rates from 20m2 to 10,000m2 suit anything from a single machine to a full construction fleet, with items up to 20 tonne lifted on site.</p>
  <ul class="checklist" style="left:642px;top:348px;color:var(--white);grid-template-columns:auto">
    <li><svg width="22" height="22"><use href="#tick"/></svg>Larger Unit Size: 10.2 x 4.5 x 3.9M<br>[Other sizes available]</li>
  </ul>
</section>

<section>
  <h2 class="abs" style="left:0;width:1200px;top:2925px;text-align:center;font-size:38px">Get In Touch</h2>
  <p class="abs" style="left:0;width:1200px;top:2989px;text-align:center;font-size:13px;color:var(--muted)">Tell us what you need to store and we will send you a square metre quote</p>
  <div class="field" style="left:333px;top:3037px;width:177px;height:39px">First Name</div>
  <div class="field" style="left:521px;top:3037px;width:177px;height:39px">Email</div>
  <div class="field" style="left:709px;top:3037px;width:177px;height:39px">Phone</div>
  <div class="field" style="left:333px;top:3080px;width:553px;height:168px">Message</div>
  <div class="btn" style="left:519px;top:3232px;width:182px;height:39px;font-size:15px">Send</div>
</section>

<div class="footer-notch"><span style="left:889px"></span><span style="left:978px"></span><span style="left:1067px"></span><span style="left:1156px"></span></div>
<footer class="site-footer">
  <div class="abs" style="left:82px;top:140px;display:flex;align-items:center;gap:10px;color:var(--red);font-family:'Rajdhani',sans-serif;font-weight:600;font-size:30px;letter-spacing:2px"><i style="width:16px;height:16px;background:var(--red);border-radius:50%"></i>KV Holding</div>
  <div class="footer-col"><h3 style="left:352px">Quick Link</h3></div>
  <ul class="footer-links"><li class="active">Home</li><li>About us</li><li>Self Storage</li><li>Workshops</li><li>Contact us</li></ul>
  <div class="footer-col"><h3 style="left:597px">Contact info</h3></div>
  <div class="footer-info">
    <div class="info-row">
      <svg width="12" height="16" viewBox="0 0 12 16"><path fill="#fff" d="M6 0a6 6 0 00-6 6c0 4.5 6 10 6 10s6-5.5 6-10a6 6 0 00-6-6zm0 8.5A2.5 2.5 0 118.5 6 2.5 2.5 0 016 8.5z"/></svg>
      <p>14 Harbour Crane Road<br>Penrose<br>Auckland 1061</p>
    </div>
    <div class="info-row" style="margin-top:24px">
      <svg width="12" height="12" viewBox="0 0 24 24"><path fill="#fff" d="M6.6 10.8a15 15 0 006.6 6.6l2.2-2.2c.3-.3.7-.4 1-.2 1.1.4 2.3.6 3.6.6.6 0 1 .4 1 1V20c0 .6-.4 1-1 1A17 17 0 013 4c0-.6.4-1 1-1h3.5c.6 0 1 .4 1 1 0 1.3.2 2.5.6 3.6.1.3 0 .7-.2 1z"/></svg>
      <p>0064 218846097</p>
    </div>
    <div class="info-row">
      <svg width="12" height="10" viewBox="0 0 14 10"><rect width="14" height="10" fill="#fff"/><path d="M0 0l7 5 7-5" fill="none" stroke="#000"/></svg>
      <p>lewis@kvholding.co.nz</p>
    </div>
  </div>
  <div class="footer-col"><h3 style="left:862px">MAP</h3></div>
  <div class="abs" style="left:865px;top:115px;width:261px;height:136px;background:linear-gradient(135deg,#e9e6dc,#dcdfe3)" role="img" aria-label="Street map showing the facility location"></div>
</footer>
<div class="copyright">
  <p>Copyright © 2020 KV Holding. All Rights Reserved.</p>
  <div class="social" aria-label="Social media links"><span></span><span></span><span></span><span></span></div>
</div>
</body>
</html>
```